Business Card Design

We need a business card design for a Executive search firm based in London & the North East called Kestrelby. We specialise in mid - snr level (£50k - £200k) IT placements. Our company colour is navy blue.

Target Market(s)

CEO, HR Director, Sales Director/VP - (35 - 50), well educated, British, European & American

Industry/Entity Type

Business

Contact Information for Business Card

Kestrelby Staffing Limited, Owen Caskell
Mobile - 0044 7731 482 616
London Office - Kestrelby House, 27 Fernmoor, Wexcombe. HA5 3LQ
Tel: 00 44 20 418 62093
North East Office – Velmora Centre, Ashgrove Way, Tillerby, NE41 2RD
Tel: 00 44 191 6842051
www.kestrelbystaffing-example.com

Also the same details for my Business Partner Ravi Tolani
with his mobile number as 0044 7852 307718

Requirements
Must have
• must have the same logo

the logo needs to be the same but made sharper

```html
<!DOCTYPE html>
<html lang="en">
<head>
<meta charset="utf-8">
<title>Kestrelby Business Card</title>
<link href="https://fonts.googleapis.com/css2?family=Quicksand:wght@400;500;600&display=swap" rel="stylesheet">
<style>
  :root {
    --bg: #e9ebee;
    --card-dark: #343434;
    --card-white: #ffffff;
    --band-grey: #e2e3e4;
    --band-slate: #647a92;
    --navy: #3b5d80;
    --logo-navy: #3f5c7c;
    --text-light: #ffffff;
    --text-soft: #e3e9f0;
  }
  * { box-sizing: border-box; margin: 0; padding: 0; }
  html, body { width: 1200px; height: 864px; overflow: hidden; }
  body {
    background: var(--bg);
    font-family: "Quicksand", "Century Gothic", sans-serif;
    display: flex; flex-direction: column; align-items: center; justify-content: center;
    gap: 44px;
  }
  .card {
    width: 630px; height: 360px;
    position: relative; overflow: hidden;
    box-shadow: 0 6px 18px rgba(0,0,0,0.18);
  }
  /* back */
  .card-back {
    background: var(--card-dark);
    display: flex; flex-direction: column; align-items: center; justify-content: center;
    gap: 44px;
  }
  .brand { display: flex; align-items: center; gap: 14px; }
  .brand-dot { width: 16px; height: 16px; border-radius: 50%; }
  .brand-name { font-weight: 500; font-size: 44px; letter-spacing: 1px; line-height: 1; }
  .card-back .brand-dot { background: var(--text-light); }
  .card-back .brand-name { color: var(--text-light); }
  .back-web { color: var(--text-light); font-size: 14px; letter-spacing: 3px; }
  /* front */
  .card-front { background: var(--card-white); display: flex; }
  .front-logo-area {
    width: 45%; display: flex; align-items: center; justify-content: center;
  }
  .card-front .brand-dot { background: var(--logo-navy); }
  .card-front .brand-name { color: var(--logo-navy); font-size: 40px; }
  .band-grey { width: 6%; background: var(--band-grey); }
  .band-slate { width: 7%; background: var(--band-slate); }
  .details {
    flex: 1; background: var(--navy); color: var(--text-light);
    padding: 34px 10px 0 22px;
  }
  .person-name { font-size: 17px; font-weight: 600; letter-spacing: 1px; }
  .person-role { font-size: 11px; font-weight: 500; letter-spacing: 1.5px; margin-top: 2px; color: var(--text-soft); }
  .address { font-size: 12.5px; line-height: 1.45; margin-top: 40px; }
  .contact-list { list-style: none; margin-top: 24px; font-size: 11px; }
  .contact-list li { display: flex; align-items: center; gap: 8px; height: 22px; white-space: nowrap; }
  .contact-list svg { width: 11px; height: 11px; flex: none; fill: var(--text-light); }
</style>
</head>
<body>
  <section class="card card-back">
    <div class="brand">
      <span class="brand-dot"></span>
      <span class="brand-name">Kestrelby</span>
    </div>
    <p class="back-web">www.kestrelbystaffing-example.com</p>
  </section>

  <section class="card card-front">
    <div class="front-logo-area">
      <div class="brand">
        <span class="brand-dot"></span>
        <span class="brand-name">Kestrelby</span>
      </div>
    </div>
    <div class="band-grey"></div>
    <div class="band-slate"></div>
    <div class="details">
      <h1 class="person-name">OWEN CASKELL</h1>
      <p class="person-role">GENERAL MANAGER</p>
      <p class="address">Kestrelby House, 27 Fernmoor,<br>Wexcombe. HA5 3LQ</p>
      <ul class="contact-list">
        <li>
          <svg viewBox="0 0 12 12"><path d="M2.5 0.5l2 2.2-1.1 1.3c.8 1.6 2 2.8 3.6 3.6l1.3-1.1 2.2 2-1.4 2C4.5 10 2 7.5 0.5 1.9z"/></svg>
          <span>00 44 20 418 62093</span>
        </li>
        <li>
          <svg viewBox="0 0 12 12"><path d="M3 0h6v12H3zM4 1.5v7.5h4V1.5zM5.5 10h1v1h-1z" fill-rule="evenodd"/></svg>
          <span>0044 7731 482 616</span>
        </li>
        <li>
          <svg viewBox="0 0 12 12"><path d="M0 2h12v8H0zM1 3.2v5.8h10V3.2L6 6.6z" fill-rule="evenodd"/></svg>
          <span>owen@kestrelbystaffing-example.com</span>
        </li>
        <li>
          <svg viewBox="0 0 12 12"><path d="M6 0a6 6 0 1 0 0 12A6 6 0 0 0 6 0zm0 1a5 5 0 0 1 0 10A5 5 0 0 1 6 1zM1 5.5h10v1H1zM5.5 1h1v10h-1z" fill-rule="evenodd"/></svg>
          <span>www.kestrelbystaffing-example.com</span>
        </li>
      </ul>
    </div>
  </section>
</body>
</html>
```